BrewDune Lane.

I want the full logo on one side. And the other side the card if right Ralf the logo the left half orange like the car in the logo color with Lorena J Torvand
Founder and CEO
Email symbol then ltorvand@brewdunelanex.com
Www symbol. Then Brewdunelanex.com
Phone symbol then 555-214-BREW
The very bottom would like Brew Dune Lane is a division of Tumbler Treks. LLC

```html
<!DOCTYPE html>
<html lang="en">
<head>
<meta charset="utf-8">
<title>Brew Dune Lane — Business Card</title>
<link rel="stylesheet" href="https://fonts.googleapis.com/css2?family=Cinzel:wght@400;600&family=Montserrat:wght@400;500&display=swap">
<style>
  :root {
    --page: #ececec;
    --card: #ffffff;
    --ink: #25272e;
    --orange: #e98c24;
    --edge: #d9571c;
    --text-light: #ffffff;
    --text-dark: #25272e;
  }
  html, body {
    margin: 0;
    width: 1200px;
    height: 900px;
    overflow: hidden;
    background: var(--page);
  }
  .stage {
    position: relative;
    width: 1200px;
    height: 900px;
  }
  .card {
    position: absolute;
    left: 300px;
    width: 600px;
    height: 343px;
    background: var(--card);
    border-bottom: 4px solid var(--edge);
    box-shadow: 0 6px 18px rgba(0,0,0,0.12);
    overflow: hidden;
  }
  .card--front { top: 70px; }
  .card--back  { top: 480px; }
  .card__shapes {
    position: absolute;
    inset: 0;
  }
  .brand {
    position: absolute;
    display: flex;
    align-items: center;
    gap: 10px;
    font-family: "Cinzel", serif;
    font-weight: 600;
    color: var(--text-dark);
    white-space: nowrap;
  }
  .brand__mark {
    width: 14px;
    height: 14px;
    border-radius: 50%;
    background: var(--orange);
    flex: none;
  }
  .card--front .brand {
    left: 120px;
    top: 128px;
    font-size: 32px;
  }
  .card--back .brand {
    left: 34px;
    top: 155px;
    font-size: 21px;
  }
  .front__web {
    position: absolute;
    left: 250px;
    top: 228px;
    display: flex;
    align-items: center;
    gap: 10px;
    font-family: "Montserrat", sans-serif;
    font-size: 14px;
    color: var(--text-light);
  }
  .person {
    position: absolute;
    left: 374px;
    top: 88px;
    color: var(--orange);
  }
  .person__name {
    font-family: "Cinzel", serif;
    font-weight: 400;
    font-size: 20px;
    margin: 0;
    line-height: 1.1;
    white-space: nowrap;
  }
  .person__role {
    font-family: "Montserrat", sans-serif;
    font-size: 11px;
    margin: 3px 0 0;
    padding-bottom: 3px;
    border-bottom: 1px solid var(--orange);
    display: inline-block;
  }
  .contacts {
    list-style: none;
    margin: 0;
    padding: 0;
    position: absolute;
    left: 374px;
    top: 158px;
    font-family: "Montserrat", sans-serif;
    font-size: 12px;
    color: var(--text-light);
  }
  .contacts li {
    display: flex;
    align-items: center;
    gap: 8px;
    margin-bottom: 9px;
    white-space: nowrap;
  }
  .icon { width: 14px; height: 14px; flex: none; }
  .division {
    position: absolute;
    left: 34px;
    bottom: 14px;
    margin: 0;
    font-family: "Montserrat", sans-serif;
    font-size: 10px;
    color: var(--text-dark);
    white-space: nowrap;
  }
</style>
</head>
<body>
<main class="stage">

  <section class="card card--front" aria-label="Card front">
    <svg class="card__shapes" viewBox="0 0 600 343" aria-hidden="true">
      <rect x="130" y="212" width="470" height="50" fill="var(--ink)"/>
      <polygon points="40,196 120,196 300,300 265,330" fill="var(--orange)"/>
      <polygon points="470,60 520,40 560,150 470,300 420,300 500,150" fill="var(--orange)"/>
    </svg>
    <div class="brand"><span class="brand__mark"></span>Brew Dune Lane</div>
    <div class="front__web">
      <svg class="icon" viewBox="0 0 16 16" aria-hidden="true"><g fill="none" stroke="currentColor" stroke-width="1.2"><circle cx="8" cy="8" r="6.5"/><ellipse cx="8" cy="8" rx="3" ry="6.5"/><line x1="1.5" y1="8" x2="14.5" y2="8"/></g></svg>
      Brewdunelanex.com
    </div>
  </section>

  <section class="card card--back" aria-label="Card back">
    <svg class="card__shapes" viewBox="0 0 600 343" aria-hidden="true">
      <polygon points="330,0 600,0 600,343 330,343 300,240 330,140" fill="var(--ink)"/>
      <polygon points="330,0 385,0 340,140 365,240 320,240 300,140" fill="var(--orange)"/>
      <polygon points="420,280 600,280 600,300 540,343 450,343" fill="var(--orange)"/>
    </svg>
    <div class="brand"><span class="brand__mark"></span>Brew Dune Lane</div>
    <div class="person">
      <h1 class="person__name">Lorena J Torvand</h1>
      <p class="person__role">Founder and CEO</p>
    </div>
    <ul class="contacts">
      <li>
        <svg class="icon" viewBox="0 0 16 16" aria-hidden="true"><path d="M4 1.5l2.2 3-1.4 1.6c.8 1.8 2.3 3.3 4.1 4.1l1.6-1.4 3 2.2-1.2 2.5C7.6 13.3 2.7 8.4 1.5 3.7z" fill="var(--orange)"/></svg>
        555-214-BREW
      </li>
      <li>
        <svg class="icon" viewBox="0 0 16 16" aria-hidden="true"><g fill="none" stroke="var(--orange)" stroke-width="1.3"><rect x="1.5" y="3.5" width="13" height="9"/><polyline points="1.5,3.5 8,9 14.5,3.5"/></g></svg>
        ltorvand@brewdunelanex.com
      </li>
      <li>
        <svg class="icon" viewBox="0 0 16 16" aria-hidden="true"><g fill="none" stroke="var(--orange)" stroke-width="1.2"><circle cx="8" cy="8" r="6.5"/><ellipse cx="8" cy="8" rx="3" ry="6.5"/><line x1="1.5" y1="8" x2="14.5" y2="8"/></g></svg>
        Brewdunelanex.com
      </li>
    </ul>
    <p class="division">Brew Dune Lane is a division of Tumbler Treks LLC</p>
  </section>

</main>
</body>
</html>
```